Brenwick Structures Construction Company Seeking Modern Website

We are a small construction company wanting to create a web presence. We don't have much in the way of current content but will get photos as they come in. Attached is a picture of our business card.
The pages we would like on the menu are:
Home
Portfolio
Product Specs
Testimonials
Our Process
Contact
Some designs we like are:
http://www.tovandrafters.example/
http://www.qrkframes.example/
http://harnestshed.example/
http://pellowbarns.example/
Not much requirements other than that so feel free to be creative!
Target Market(s)
Construction
Commercial and Residential Buildings
Industry/Entity Type
Construction Company
Number of Pages Required
5+ page

```html
<!DOCTYPE html>
<html lang="en">
<head>
<meta charset="utf-8">
<title>Brenwick Structures</title>
<link href="https://fonts.googleapis.com/css2?family=Questrial&family=Open+Sans:ital,wght@0,400;0,600;1,400&display=swap" rel="stylesheet">
<style>
:root{
  --blue:#0aa0dd;
  --blue-bright:#00a8e6;
  --coral:#e9675b;
  --black:#0b0b0b;
  --ink:#222;
  --grey-text:#555;
  --band-grey:#eeeeee;
  --footer-dark:#141414;
  --white:#fff;
}
*{margin:0;padding:0;box-sizing:border-box}
html,body{width:723px;height:1200px;overflow:hidden;background:var(--white)}
body{position:relative;font-family:"Open Sans",Arial,sans-serif;color:var(--ink)}
.abs{position:absolute}
.heading{font-family:"Questrial","Century Gothic",sans-serif}

/* header */
.site-header{left:0;top:0;width:723px;height:56px;background:var(--white)}
.brand{left:28px;top:15px;display:flex;align-items:center;gap:5px;font-family:"Questrial",sans-serif;font-size:11px;color:#1f3c88;white-space:nowrap}
.brand-mark{width:12px;height:12px;background:#1f3c88}
.main-nav{right:28px;top:23px;display:flex;gap:29px;font-size:7px;letter-spacing:.1px}
.main-nav a{color:var(--blue);text-decoration:none}
.main-nav a.active{color:#e63b2e}

/* hero */
.hero{left:0;top:56px;width:723px;height:376px;overflow:hidden}
.hero-photo{position:absolute;inset:0;background:linear-gradient(115deg,#2a2a2a 0%,#6a5a50 18%,#e8e8e4 38%,#cfd3cf 55%,#a8c62a 60%,#dcdcd8 70%,#f0f0ee 100%)}
.hero-shape{position:absolute;left:0;top:0}
.hero-title{right:27px;top:78px;text-align:right;color:var(--white);font-size:47px;line-height:60px;letter-spacing:1px}
.hero-text{right:27px;top:192px;width:300px;text-align:right;color:var(--white);font-size:8.4px;line-height:13.6px}
.btn-light{right:27px;top:237px;width:68px;height:20px;background:var(--white);color:var(--coral);font-size:8.5px;display:flex;align-items:center;justify-content:center}
.hero-dots{left:616px;top:325px;display:flex;gap:5px}
.hero-dots span{width:15px;height:2px;background:#111}
.hero-dots span.on{background:var(--white)}

/* services */
.services{left:0;top:432px;width:723px;height:128px;background:var(--black)}
.service{width:160px;text-align:center}
.service-icon{position:absolute;left:55px;top:-18px;width:50px;height:50px;border-radius:50%;background:var(--blue);border:2px solid var(--white);display:flex;align-items:center;justify-content:center}
.service-icon.first{background:var(--white);border-color:var(--blue)}
.service-title{position:absolute;left:0;top:40px;width:160px;font-size:10.5px;color:var(--blue)}
.service-text{position:absolute;left:12px;top:57px;width:136px;font-size:7px;line-height:10px;color:var(--white)}
.btn-more{position:absolute;left:58px;top:94px;width:44px;height:16px;border:1px solid var(--blue);color:var(--white);font-size:7px;font-weight:600;display:flex;align-items:center;justify-content:center;gap:3px}
.btn-more.solid{background:var(--blue)}
.slider-arrow{top:52px}

/* welcome */
.welcome-title{left:0;top:584px;width:723px;text-align:center;font-size:21px;color:var(--ink)}
.welcome-title span{color:var(--blue)}
.welcome-text{left:70px;top:620px;width:583px;text-align:center;font-size:7px;line-height:13.6px;color:var(--grey-text)}
.btn-read{left:326px;top:666px;width:69px;height:22px;background:var(--blue);color:var(--white);font-size:7px;font-weight:600;display:flex;align-items:center;justify-content:center}

/* testimonial */
.testimonials{left:0;top:720px;width:723px;height:199px;background:var(--band-grey)}
.quote-card{left:207px;top:763px;width:240px;height:102px;background:var(--white);padding:26px 14px 0 14px;font-style:italic;font-size:7px;line-height:13.6px;color:#999}
.quote-card::after{content:"";position:absolute;right:-14px;top:30px;border-left:14px solid var(--white);border-top:14px solid transparent}
.quote-mark{left:202px;top:752px;font-family:Georgia,serif;font-size:44px;line-height:44px;color:var(--blue);font-weight:bold}
.avatar{left:478px;top:767px;width:44px;height:44px;border-radius:50%;background:linear-gradient(#c69a78,#8a6a52 60%,#2a2a2a);border:2px solid var(--white)}
.person-name{left:474px;top:818px;font-size:11.5px;color:var(--blue)}
.person-loc{left:474px;top:834px;font-size:7px;color:#888}

/* footer */
.site-footer{left:0;top:919px;width:723px;height:234px;background:var(--footer-dark)}
.footer-map{position:absolute;inset:0;background:radial-gradient(ellipse at 40% 40%,#222 0%,#141414 70%)}
.footer-heading{font-size:18px;color:var(--blue-bright);font-weight:bold}
.contact-heading{right:415px;top:963px}
.contact-lines{right:415px;top:998px;text-align:right;font-size:10.5px;line-height:17px;color:var(--white)}
.socials{left:233px;top:1077px;display:flex;gap:5px}
.socials span{width:22px;height:22px;border-radius:50%;border:1px solid var(--white)}
.socials span.red{background:#d9302a}
.footer-divider{left:349px;top:963px;width:1px;height:152px;background:#3a3a3a}
.news-heading{left:386px;top:963px}
.news-text{left:388px;top:997px;width:210px;font-size:7.6px;line-height:14px;color:#ddd}
.email-field{left:390px;top:1033px;width:198px;height:27px;border:1px solid #333;background:#0e0e0e;color:#888;font-size:7.6px;padding:8px 0 0 13px}
.btn-subscribe{left:390px;top:1073px;width:198px;height:27px;background:var(--blue-bright);color:var(--white);font-size:7.6px;font-weight:600;display:flex;align-items:center;justify-content:center}

.bottom-bar{left:0;top:1153px;width:723px;height:47px;background:var(--blue-bright);color:var(--white);font-size:6.4px;font-weight:600}
.legal-links{position:absolute;left:30px;top:21px}
.copyright{position:absolute;right:29px;top:19px}
</style>
</head>
<body>

<header class="site-header abs">
  <div class="brand abs"><span class="brand-mark"></span>Brenwick Structures</div>
  <nav class="main-nav abs">
    <a class="active">HOME</a><a>PORTFOLIO</a><a>PRODUCT SPECS</a><a>TESTIMONIALS</a><a>OUR PROCESS</a><a>CONTACT</a>
  </nav>
</header>

<section class="hero abs">
  <div class="hero-photo" role="img" aria-label="Architect in a suit drawing building plans on blueprints with a green folder on the desk"></div>
  <svg class="hero-shape" width="723" height="376" viewBox="0 0 723 376">
    <circle cx="780" cy="330" r="430" fill="#e9675b" opacity=".92"/>
    <line x1="0" y1="375" x2="723" y2="375" stroke="#fff" stroke-width="2"/>
  </svg>
  <h1 class="hero-title heading abs">BUILDING<br>DREAMS</h1>
  <p class="hero-text abs">Lorem ipsum dolor sit amet, consectetur adipiscing elit, sed do eiusmod tempor incididunt ut labore et dolore magna aliqua. Ut enim ad minim veniam, quis nostrud exercitation ullamco laboris</p>
  <div class="btn-light abs heading">Read More</div>
  <div class="hero-dots abs"><span></span><span class="on"></span><span></span></div>
</section>

<section class="services abs">
  <svg class="slider-arrow abs" style="left:13px" width="11" height="14"><polygon points="11,0 11,14 0,7" fill="#fff"/></svg>
  <svg class="slider-arrow abs" style="left:700px" width="11" height="14"><polygon points="0,0 0,14 11,7" fill="#fff"/></svg>

  <div class="service abs" style="left:26px;top:0">
    <div class="service-icon first">
      <svg width="20" height="16" viewBox="0 0 20 16" fill="#0aa0dd"><circle cx="10" cy="4" r="3"/><circle cx="4" cy="5" r="2.3"/><circle cx="16" cy="5" r="2.3"/><rect x="6" y="8" width="8" height="7" rx="2"/><rect x="0.5" y="9" width="6" height="5" rx="2"/><rect x="13.5" y="9" width="6" height="5" rx="2"/></svg>
    </div>
    <div class="service-title heading">Consecteture Adipiscing 1</div>
    <div class="service-text">Lorem ipsum dolor sit amet, consecte-tur ipsum dolor sit amet, consectetur adipis do edit at labour</div>
    <div class="btn-more solid">MORE <svg width="4" height="6"><polygon points="0,0 4,3 0,6" fill="#fff"/></svg></div>
  </div>

  <div class="service abs" style="left:193px;top:0">
    <div class="service-icon">
      <svg width="22" height="22" viewBox="0 0 22 22"><circle cx="11" cy="11" r="8" fill="none" stroke="#fff" stroke-width="3"/><circle cx="11" cy="11" r="3.5" fill="#fff"/></svg>
    </div>
    <div class="service-title heading">Consecteture Adipiscing 2</div>
    <div class="service-text">Lorem ipsum dolor sit amet, consecte-tur ipsum dolor sit amet, consectetur adipis do edit at labour</div>
    <div class="btn-more">MORE <svg width="4" height="6"><polygon points="0,0 4,3 0,6" fill="#fff"/></svg></div>
  </div>

  <div class="service abs" style="left:361px;top:0">
    <div class="service-icon">
      <svg width="24" height="20" viewBox="0 0 24 20" fill="none" stroke="#fff" stroke-width="2"><rect x="7" y="1" width="9" height="8"/><rect x="2" y="10" width="9" height="8"/><rect x="13" y="10" width="9" height="8"/></svg>
    </div>
    <div class="service-title heading">Consecteture Adipiscing 3</div>
    <div class="service-text">Lorem ipsum dolor sit amet, consecte-tur ipsum dolor sit amet, consectetur adipis do edit at labour</div>
    <div class="btn-more">MORE <svg width="4" height="6"><polygon points="0,0 4,3 0,6" fill="#fff"/></svg></div>
  </div>

  <div class="service abs" style="left:533px;top:0">
    <div class="service-icon">
      <svg width="20" height="20" viewBox="0 0 20 20" fill="#fff"><rect x="2" y="5" width="16" height="12" rx="1"/><rect x="1" y="2" width="18" height="4" rx="1"/></svg>
    </div>
    <div class="service-title heading">Consecteture Adipiscing 4</div>
    <div class="service-text">Lorem ipsum dolor sit amet, consecte-tur ipsum dolor sit amet, consectetur adipis do edit at labour</div>
    <div class="btn-more">MORE <svg width="4" height="6"><polygon points="0,0 4,3 0,6" fill="#fff"/></svg></div>
  </div>
</section>

<h2 class="welcome-title heading abs">Welcome to <span>Brenwick Structures</span></h2>
<p class="welcome-text abs">Lorem ipsum dolor sit amet, consectetur adipiscing elit, sed do eiusmod tempor incididunt ut labore et dolore magna aliqua. Ut enim ad minim veniam, quis nostrud exercitation ullamco laboris nisi ut aliquip ex ea commodo consequat. Duis aute irure dolor in reprehenderit in voluptate velit esse cillum dolore eu</p>
<div class="btn-read abs">READ MORE</div>

<section class="testimonials abs"></section>
<svg class="abs" style="left:105px;top:782px" width="24" height="65"><polyline points="23,0 1,32 23,64" fill="none" stroke="#bbb" stroke-width="1"/></svg>
<svg class="abs" style="left:591px;top:778px" width="24" height="65"><polyline points="1,0 23,32 1,64" fill="none" stroke="#bbb" stroke-width="1"/></svg>
<div class="quote-mark abs">&ldquo;</div>
<blockquote class="quote-card abs">Lorem ipsum dolor sit amet, consectetur adipiscing elit, sed do eiusmod tempor incididunt ut labore et dolore magna aliqua. Ut enim ad minim veniam, quis nostrud exercitation ullamco laboris nisi ut aliquip ex ea commodo consequat.</blockquote>
<div class="avatar abs" role="img" aria-label="Portrait photo of the client"></div>
<div class="person-name heading abs">Dana Whitlow</div>
<div class="person-loc abs">City&nbsp; Location</div>

<footer class="site-footer abs">
  <div class="footer-map" role="img" aria-label="Dark faded regional road map in the background"></div>
</footer>
<h3 class="footer-heading heading contact-heading abs">Contact Us</h3>
<div class="contact-lines abs">CALL TOLL-FREE<br>1-234-567-890<br>No.5&nbsp; Address Line1<br>Address Line-2&nbsp; 123450</div>
<div class="socials abs"><span class="red"></span><span></span><span></span></div>
<div class="footer-divider abs"></div>
<h3 class="footer-heading heading news-heading abs">News Letter&nbsp; Signup</h3>
<p class="news-text abs">Lorem ipsum dolor sit amet, consectetur adipiscing elitsed do eiusmod tempor incididunt</p>
<div class="email-field abs">Email Address</div>
<div class="btn-subscribe abs">SUBSCRIBE</div>

<div class="bottom-bar abs">
  <span class="legal-links">Policies&nbsp; |&nbsp; Privacy&nbsp; |&nbsp; Terms &amp; Conditions</span>
  <span class="copyright">Copyright 2015 Comapny name. All Rights Reserved.</span>
</div>

</body>
</html>
```